Private Equity Company Stationary
business card, letterhead, envelope, fax cover
#46 please eliminate the email address from the envelope. Thanks
#34 Birchway Holdings Group Header and remove big logo/watermark from the center of the page.
#33 remove all the phone numbers from envelope
#21 please eliminate border (header and footer) from business card, letterhead, fax coverand just leave it plain. Please re-submit with changes
envelope flaps to remain white
The only place the cell phone number is needed is on the business card.
I need some clarification before I can submit a satifactory design.
1. Do we need to mention the name "Holdings Grouup Advisory, Inc." compulsarily in any of the media.
2. Are there any limitations on the no of colours that can be used as printing costs can vary significantly.

```html
<!DOCTYPE html>
<html lang="en">
<head>
<meta charset="utf-8">
<title>Birchway Holdings Group – Stationery</title>
<link href="https://fonts.googleapis.com/css2?family=Cormorant+Garamond:ital,wght@0,500;0,600;1,500&display=swap" rel="stylesheet">
<style>
  :root{
    --backdrop:#d9d9d6;
    --paper:#ffffff;
    --navy:#2c3b5e;
    --gold:#a68a55;
    --ink:#6d6f75;
    --fold:#e2e2e2;
  }
  html,body{margin:0;padding:0;overflow:hidden}
  body{width:1200px;height:871px;background:var(--backdrop);position:relative;
       font-family:"Cormorant Garamond",Georgia,serif;color:var(--ink)}
  .sheet{position:absolute;background:var(--paper);box-shadow:0 3px 12px rgba(0,0,0,.28)}
  .wordmark{position:absolute;display:flex;align-items:center;gap:8px;color:var(--navy);
            font-weight:600;text-transform:uppercase;letter-spacing:.02em;white-space:nowrap}
  .wordmark .square{background:var(--navy);display:block}
  .contact{position:absolute;font-size:9px;line-height:11px;white-space:nowrap}
  .contact .label{color:var(--navy);font-weight:600;margin-top:9px}
  .contact .label:first-child{margin-top:0}
  .align-right{text-align:right}

  /* letterhead */
  .letterhead{left:53px;top:36px;width:566px;height:790px}
  .letterhead .wordmark{right:20px;top:56px;font-size:22px}
  .letterhead .wordmark .square{width:22px;height:22px}
  .letterhead .contact{right:44px;top:138px}
  .letterhead .footer-note{position:absolute;right:44px;bottom:30px;font-size:9px;line-height:11px;text-align:right}

  /* business card */
  .business-card{left:727px;top:115px;width:252px;height:156px}
  .business-card .wordmark{right:12px;top:18px;font-size:12px;gap:5px}
  .business-card .wordmark .square{width:12px;height:12px}
  .business-card .contact{right:14px;top:50px;font-size:6px;line-height:7px}
  .business-card .contact .label{margin-top:5px}
  .holder{position:absolute;left:12px;top:94px;font-size:9px;line-height:10px;color:var(--ink)}
  .holder .name{color:var(--navy);font-size:11px;font-weight:600}
  .holder .title{font-style:italic;margin-bottom:3px}

  /* envelope */
  .envelope{left:463px;top:312px;width:701px;height:420px}
  .envelope svg.flap{position:absolute;left:0;top:0}
  .envelope .return-line{position:absolute;left:0;width:100%;top:40px;text-align:center;
                         font-size:8px;color:var(--navy);font-weight:600;letter-spacing:.05em}
  .envelope .wordmark{left:34px;top:168px;font-size:24px}
  .envelope .wordmark .square{width:24px;height:24px}
  .envelope .contact{left:34px;top:262px}
</style>
</head>
<body>

<section class="sheet letterhead" aria-label="Letterhead">
  <div class="wordmark"><span class="square"></span>Birchway Holdings Group</div>
  <div class="contact align-right">
    <div class="label">Address</div>
    <div>240 Harbor Ave, Suite 310</div>
    <div>Lakeview, CA 90410</div>
    <div class="label">Phone</div>
    <div>(555) 014-2290</div>
    <div class="label">Fax</div>
    <div>(555) 014-2291</div>
    <div class="label">Web</div>
    <div>www.birchwayhg.com</div>
  </div>
  <div class="footer-note">Facsimile No.<br>(555) 014-2291</div>
</section>

<section class="sheet envelope" aria-label="Envelope">
  <svg class="flap" width="701" height="420" viewBox="0 0 701 420" aria-hidden="true">
    <polyline points="0,132 70,4 631,4 701,132" fill="none" stroke="var(--fold)" stroke-width="1.5"/>
    <line x1="0" y1="132" x2="701" y2="132" stroke="#cfcfcf" stroke-width="1.5"/>
  </svg>
  <div class="return-line">www.birchwayhg.com</div>
  <div class="wordmark"><span class="square"></span>Birchway Holdings Group</div>
  <div class="contact">
    <div class="label">Address</div>
    <div>240 Harbor Ave, Suite 310</div>
    <div>Lakeview, CA 90410</div>
    <div class="label">Web</div>
    <div>www.birchwayhg.com</div>
  </div>
</section>

<section class="sheet business-card" aria-label="Business card">
  <div class="wordmark"><span class="square"></span>Birchway Holdings Group</div>
  <div class="contact align-right">
    <div class="label">Address</div>
    <div>240 Harbor Ave, Suite 310</div>
    <div>Lakeview, CA 90410</div>
    <div class="label">Phone</div>
    <div>(555) 014-2290</div>
    <div class="label">Fax</div>
    <div>(555) 014-2291</div>
  </div>
  <div class="holder">
    <div class="name">Adrian Valmorent</div>
    <div class="title">Managing Director</div>
    <div>m (555) 014-2292</div>
    <div>a.valmorent@birchwayhg.com</div>
  </div>
</section>

</body>
</html>
```